Business Card Design Project

Basic business card with minimal details. I just need company name, email & web address, telephone and my name.
I would like the back of the card to be grey with my logo & company name centred.

Target Market(s)

Architects
Builders
Property Developers

Industry/Entity Type

Business

Font styles to use
Sans Serif

Colors

Designer to choose colors to be used in the design.

Requirements
Must have
• Venture Frame
Marcus Hadley - Director
M: 0452 913084
E: marcus@ventureframe.com.au
W: www.ventureframe.com.au
Should not have
• No other images or pictures

```html
<!DOCTYPE html>
<html lang="en">
<head>
<meta charset="utf-8">
<title>Venture Frame – Business Card</title>
<link href="https://fonts.googleapis.com/css2?family=Arimo:wght@400;700&display=swap" rel="stylesheet">
<style>
  :root {
    --page-bg: #ece9e4;
    --card-bg: #dedede;
    --brand-red: #b3163a;
    --slate: #4b5661;
    --text-grey: #555d66;
    --card-shadow: rgba(0, 0, 0, 0.18);
  }
  * { margin: 0; padding: 0; box-sizing: border-box; }
  html, body {
    width: 1200px;
    height: 870px;
    overflow: hidden;
    background: var(--page-bg);
    font-family: "Arimo", Arial, sans-serif;
  }
  .canvas {
    width: 1200px;
    height: 870px;
    display: flex;
    align-items: center;
    justify-content: center;
  }
  .card {
    width: 478px;
    height: 780px;
    background: var(--card-bg);
    box-shadow: 0 6px 22px var(--card-shadow);
    display: flex;
    flex-direction: column;
    align-items: center;
    text-align: center;
    padding-top: 120px;
  }
  .brand {
    display: flex;
    flex-direction: column;
    align-items: center;
    gap: 26px;
  }
  .brand-mark {
    width: 64px;
    height: 64px;
    background: var(--brand-red);
  }
  .brand-name {
    font-weight: 400;
    font-size: 36px;
    letter-spacing: 4px;
    color: var(--slate);
    text-transform: uppercase;
  }
  .person {
    margin-top: 62px;
  }
  .person-name {
    font-weight: 700;
    font-size: 22px;
    letter-spacing: 1px;
    color: var(--brand-red);
    text-transform: uppercase;
  }
  .person-title {
    margin-top: 4px;
    font-size: 15px;
    color: var(--text-grey);
  }
  .contact {
    margin-top: auto;
    margin-bottom: 150px;
    list-style: none;
    font-size: 19px;
    line-height: 1.45;
    color: var(--text-grey);
  }
</style>
</head>
<body>
  <main class="canvas">
    <article class="card">
      <header class="brand">
        <div class="brand-mark" aria-hidden="true"></div>
        <h1 class="brand-name">Venture Frame</h1>
      </header>
      <section class="person">
        <h2 class="person-name">Marcus Hadley</h2>
        <p class="person-title">Director</p>
      </section>
      <ul class="contact">
        <li class="contact-phone">0452 913084</li>
        <li class="contact-email">marcus@ventureframe.com.au</li>
        <li class="contact-web">www.ventureframe.com.au</li>
      </ul>
    </article>
  </main>
</body>
</html>
```